Flyer Handout when attending Dental Conventions, or dental office shows

take the sample file folder that is shown with 2 pictures. The outside and inside of the folder needs to be completed, along with the inserts. This folder pictures are from someone elses flyer/folder and i would like to have it layout like this. The KRV inserts is informational, but it is lacking originality, pictures, etc. Try to make our information and move it to 2017. When this is done, i would like to take this flyer and load it to the web or allow to send via email and make it interactive. The user can select the flyers and it will slide or flip to the flyer. this will make if kewl/fun

Target Market(s)

Dental Offices

Industry/Entity Type

Dental

Font styles to use
Serif
Sans Serif

Colors

Designer to choose colors to be used in the design.

Requirements
Must have
• a Semi new look and feel of our flyers, and a new envelope created

```html
<!DOCTYPE html>
<html lang="en">
<head>
<meta charset="utf-8">
<title>KRV Presentation Folder</title>
<link rel="stylesheet" href="https://fonts.googleapis.com/css2?family=Lato:wght@300;400;700&family=Roboto+Condensed:wght@700&display=swap">
<style>
  :root{
    --brand-blue:#2a9fd8;
    --brand-blue-deep:#1b7fbf;
    --accent-orange:#f7922f;
    --paper:#ffffff;
    --paper-shade:#f3f5f7;
    --ink:#3a3a3a;
    --backdrop:#e8e6e3;
  }
  html,body{margin:0;padding:0;width:1200px;height:1200px;overflow:hidden;background:var(--backdrop);}
  .folder{display:block;width:1200px;height:1200px;}
  .body-text{font-family:"Lato",sans-serif;}
  .headline-light{font-family:"Lato",sans-serif;font-weight:300;}
  .headline-bold{font-family:"Roboto Condensed",sans-serif;font-weight:700;}
  .brand-name{font-family:"Lato",sans-serif;font-weight:700;}
</style>
</head>
<body>
<svg class="folder" viewBox="0 0 1500 1500" xmlns="http://www.w3.org/2000/svg">
  <defs>
    <linearGradient id="band" x1="0" y1="0" x2="1" y2="0">
      <stop offset="0" stop-color="var(--brand-blue-deep)"/>
      <stop offset="0.5" stop-color="var(--brand-blue)"/>
      <stop offset="1" stop-color="var(--brand-blue-deep)"/>
    </linearGradient>
    <linearGradient id="photoTone" x1="0" y1="0" x2="0" y2="1">
      <stop offset="0" stop-color="#ffffff"/>
      <stop offset="0.2" stop-color="#f2d6d8"/>
      <stop offset="0.5" stop-color="#c9cfdc"/>
      <stop offset="0.85" stop-color="#d8606a"/>
      <stop offset="1" stop-color="#e9a0a6"/>
    </linearGradient>
    <linearGradient id="foldShade" x1="0" y1="0" x2="1" y2="0">
      <stop offset="0" stop-color="#d9d9d9"/>
      <stop offset="1" stop-color="#ffffff" stop-opacity="0"/>
    </linearGradient>
    <linearGradient id="pageTint" x1="0" y1="0" x2="0" y2="1">
      <stop offset="0" stop-color="var(--paper-shade)"/>
      <stop offset="1" stop-color="#ffffff"/>
    </linearGradient>
  </defs>

  <!-- Outside spread -->
  <g class="outside-spread">
    <rect class="paper" x="263" y="55" width="974" height="688" fill="var(--paper)"/>
    <rect class="back-page-tint" x="263" y="92" width="487" height="466" fill="url(#pageTint)"/>
    <rect class="cover-photo" x="750" y="200" width="487" height="425" fill="url(#photoTone)" role="img" aria-label="Photo of a dentist in mask and gloves holding a mirror and probe, seen from inside a patient's open mouth"/>
    <path class="top-band" d="M263 55 H1237 V92 H840 C800 92 790 158 750 158 C710 158 700 92 660 92 H263 Z" fill="url(#band)"/>
    <path class="bottom-band" d="M263 558 H655 C700 558 720 625 750 625 C780 625 800 558 845 558 H1237 V743 H263 Z" fill="url(#band)"/>
    <path class="accent-strip" d="M263 708 H610 C640 708 655 728 670 743 H263 Z" fill="var(--accent-orange)"/>
    <path class="accent-strip" d="M1237 708 H890 C860 708 845 728 830 743 H1237 Z" fill="var(--accent-orange)"/>

    <text class="brand-name" x="1020" y="180" font-size="66" fill="var(--brand-blue)" text-anchor="middle">KRV</text>

    <text class="body-text" x="320" y="308" font-size="13" font-weight="700" fill="var(--brand-blue)">Company Overview</text>
    <g class="body-text" font-size="9.6" fill="var(--ink)">
      <text x="320" y="333" textLength="372">KRV is one of the largest electronic dental clearinghouses for dental claims and a</text>
      <text x="320" y="346" textLength="372">leader in providing dental EDI solutions. We focus on bringing together Payers,</text>
      <text x="320" y="358" textLength="372">Providers and Vendors to promote EDI transactions. Thousands of Dentists have</text>
      <text x="320" y="371" textLength="372">chosen KRV as their electronic dental claims vendor of choice. Using our</text>
      <text x="320" y="383" textLength="372">technology, KRV allows you to submit dental claims in seconds, the submission of</text>
      <text x="320" y="396" textLength="372">Real Time Claim Statuses, Real Time Eligibility and getting Electronic Remittance</text>
      <text x="320" y="408">Advice's (ERA's).</text>
    </g>

    <text class="brand-name" x="322" y="655" font-size="52" fill="#ffffff">KRV</text>

    <g class="contact-list body-text" font-size="11.5" fill="#ffffff">
      <path d="M496 600 L504 593 L512 600 V607 H496 Z" fill="var(--accent-orange)"/>
      <text x="521" y="603">218 Alder Lane</text>
      <text x="521" y="617">Brookfield, MN 55190</text>
      <circle cx="504" cy="634" r="6" fill="none" stroke="var(--accent-orange)" stroke-width="2"/>
      <text x="521" y="639">800-555-0142 (Toll Free)</text>
      <rect x="497" y="654" width="14" height="9" rx="3" fill="var(--accent-orange)"/>
      <text x="521" y="664">651-555-0178</text>
      <circle cx="504" cy="682" r="6" fill="none" stroke="var(--accent-orange)" stroke-width="1.5"/>
      <line x1="498" y1="682" x2="510" y2="682" stroke="var(--accent-orange)" stroke-width="1.2"/>
      <text x="521" y="686">www.krvdental.com</text>
    </g>

    <text class="headline-light" x="1020" y="628" font-size="30" fill="#ffffff" text-anchor="middle">Bridging the Gap Between</text>
    <text class="headline-bold" x="1020" y="670" font-size="35" fill="#ffffff" text-anchor="middle">PAYERS AND PROVIDERS</text>
    <text class="body-text" x="1025" y="729" font-size="12" letter-spacing="4" fill="#3a3a3a" text-anchor="middle">www.krvdental.com</text>
  </g>

  <!-- Inside spread -->
  <g class="inside-spread">
    <rect class="paper" x="263" y="777" width="974" height="689" fill="var(--paper)"/>
    <rect class="fold-shade" x="750" y="777" width="140" height="689" fill="url(#foldShade)"/>
    <path class="pocket-left" d="M263 1293 H640 C700 1293 722 1340 734 1400 L750 1466 H263 Z" fill="url(#band)"/>
    <path class="pocket-right" d="M1237 1293 H880 C820 1293 798 1340 782 1400 L750 1466 H1237 Z" fill="url(#band)"/>

    <text class="brand-name" x="848" y="1398" font-size="52" fill="#ffffff">KRV</text>

    <g class="contact-list body-text" font-size="11.5" fill="#ffffff">
      <path d="M1032 1341 L1040 1334 L1048 1341 V1348 H1032 Z" fill="var(--accent-orange)"/>
      <text x="1059" y="1344">218 Alder Lane</text>
      <text x="1059" y="1359">Brookfield, MN 55190</text>
      <circle cx="1040" cy="1377" r="6" fill="none" stroke="var(--accent-orange)" stroke-width="2"/>
      <text x="1059" y="1382">800-555-0142 (Toll Free)</text>
      <rect x="1033" y="1399" width="14" height="9" rx="3" fill="var(--accent-orange)"/>
      <text x="1059" y="1409">651-555-0178</text>
      <circle cx="1040" cy="1428" r="6" fill="none" stroke="var(--accent-orange)" stroke-width="1.5"/>
      <line x1="1034" y1="1428" x2="1046" y2="1428" stroke="var(--accent-orange)" stroke-width="1.2"/>
      <text x="1059" y="1432">www.krvdental.com</text>
    </g>
  </g>
</svg>
</body>
</html>
```